Portal Panel Medic need professional looking business card printed on plastic, Commericial, Industri

We are family owned and operated garage door company in Indianapolis, Indiana. We sale service and install dock equipment, doors, operators. We are looking to expand our commercial/ industrial division. We also service all residential doors and operators. We are looking for a business that stands out of the crowd. We are committed to have the best customer service in the industry.

Target Market(s)

National and local general contractors, National/ Corpate service accounts,

Industry/Entity Type

Business Service

Contact Information for Business Card

To be printed on plastic stock

Font styles to use
Sans Serif

Colors
ffffff
f04a50
ec1f27

Requirements
Must have
• Name, website,email, phone number, position.
Nice to have
• A standout professional design

```html
<!DOCTYPE html>
<html lang="en">
<head>
<meta charset="utf-8">
<title>Portal Panel Medic – Business Card</title>
<link rel="stylesheet" href="https://fonts.googleapis.com/css2?family=Open+Sans:ital,wght@0,400;0,600;0,700;1,400;1,600&family=Playfair+Display:ital,wght@1,400&display=swap">
<style>
  :root {
    --white: #ffffff;
    --brand-red: #ec1f27;
    --soft-red: #f04a50;
    --card-red: #ea3338;
    --ink: #2b2b2b;
    --backdrop: #e6e6e6;
  }
  * { box-sizing: border-box; margin: 0; padding: 0; }
  html, body { width: 1200px; height: 801px; overflow: hidden; }
  body {
    background: var(--backdrop);
    font-family: "Open Sans", Arial, sans-serif;
    position: relative;
  }
  .card {
    position: absolute;
    top: 260px;
    width: 495px;
    height: 282px;
    border-radius: 10px;
    box-shadow: 0 6px 18px rgba(0,0,0,0.25);
  }
  .card--front { left: 89px; background: var(--white); }
  .card--back { left: 649px; background: var(--card-red); color: var(--white); }

  .brand {
    position: absolute;
    display: flex;
    align-items: center;
    gap: 12px;
    font-weight: 700;
    white-space: nowrap;
  }
  .brand__dot { flex: none; border-radius: 50%; }
  .card--front .brand {
    left: 0; right: 0; top: 96px;
    justify-content: center;
    font-size: 30px;
    color: var(--brand-red);
  }
  .card--front .brand__dot { width: 34px; height: 34px; background: var(--brand-red); }
  .card--back .brand {
    left: 23px; width: 232px; top: 92px;
    justify-content: center;
    font-size: 21px;
    color: var(--white);
  }

  .tagline { font-style: italic; }
  .card--front .tagline {
    position: absolute; left: 0; right: 0; top: 200px;
    text-align: center; font-size: 14.5px; font-weight: 600; color: var(--ink);
  }
  .card--front .phone-large {
    position: absolute; left: 0; right: 0; top: 227px;
    text-align: center;
    font-family: "Playfair Display", Georgia, serif;
    font-style: italic; font-size: 25px; color: var(--brand-red);
  }
  .card--back .tagline {
    position: absolute; right: 240px; top: 175px;
    text-align: right; font-size: 19px; font-weight: 600; line-height: 30px;
  }

  .person { position: absolute; left: 323px; top: 58px; }
  .person__name { font-size: 20px; font-weight: 700; line-height: 26px; }
  .person__role { font-size: 13px; font-weight: 700; line-height: 18px; }

  .contacts { position: absolute; left: 300px; top: 162px; list-style: none; }
  .contacts li {
    display: flex; align-items: center; gap: 6px;
    font-size: 14px; font-weight: 600; line-height: 19.5px;
  }
  .contacts svg { width: 14px; height: 14px; flex: none; }
</style>
</head>
<body>
  <section class="card card--front">
    <div class="brand"><span class="brand__dot"></span>Portal Panel Medic</div>
    <p class="tagline">Expert Service at an affordable price</p>
    <p class="phone-large">(555) 014-2870</p>
  </section>

  <section class="card card--back">
    <div class="brand">Portal Panel Medic</div>
    <p class="tagline">Expert Service<br>at an affordable price</p>
    <div class="person">
      <p class="person__name">NAME</p>
      <p class="person__role">Designation</p>
    </div>
    <ul class="contacts">
      <li>
        <svg viewBox="0 0 14 14"><circle cx="7" cy="7" r="7" fill="#fff"/><path d="M4.3 4.2c.4-.4.9-.4 1.1 0l.6 1c.2.3.1.6-.2.8l-.3.3c.4.9 1.1 1.6 2 2l.3-.3c.2-.3.5-.4.8-.2l1 .6c.4.2.4.7 0 1.1-.6.6-1.5.7-2.4.2-1.2-.6-2.2-1.6-2.8-2.8-.5-.9-.4-1.8.2-2.4z" fill="var(--card-red)"/></svg>
        (555) 014-2870
      </li>
      <li>
        <svg viewBox="0 0 14 14"><circle cx="7" cy="7" r="7" fill="#fff"/><g fill="none" stroke="var(--card-red)" stroke-width="0.9"><circle cx="7" cy="7" r="4"/><ellipse cx="7" cy="7" rx="1.8" ry="4"/><path d="M3 7h8"/></g></svg>
        Website
      </li>
      <li>
        <svg viewBox="0 0 14 14"><circle cx="7" cy="7" r="7" fill="#fff"/><g fill="none" stroke="var(--card-red)" stroke-width="0.9"><rect x="3.5" y="4.5" width="7" height="5"/><path d="M3.5 4.5 7 7.3l3.5-2.8"/></g></svg>
        Email
      </li>
    </ul>
  </section>
</body>
</html>
```